Kelvar Systems Website

Website design for our company: Kelvar Systems.
The website should look fresh and IT focused. Please have a look at http://www.kelvarsystems.net.au/ for our current design. We want something fresh and new, professional looking, in WordPress so we can easily make changes.

Industry/Entity Type

It Company

```html
<!DOCTYPE html>
<html lang="en">
<head>
<meta charset="utf-8">
<title>Kelvar Systems</title>
<link href="https://fonts.googleapis.com/css2?family=Open+Sans:wght@400;600;700&family=Roboto+Condensed:wght@700&display=swap" rel="stylesheet">
<style>
  :root {
    --green: #5cb531;
    --green-dark: #4a9a24;
    --black: #111111;
    --panel: #2a2a2a;
    --footer: #1c1c1c;
    --text: #666666;
    --heading: #2b2b2b;
    --light: #e9e9e9;
    --white: #ffffff;
  }
  * { margin: 0; padding: 0; box-sizing: border-box; }
  html, body { width: 710px; height: 1200px; overflow: hidden; }
  body { position: relative; background: var(--white); font-family: "Open Sans", Arial, sans-serif; color: var(--text); }

  .site-header { position: absolute; top: 0; left: 0; width: 710px; height: 66px; background: var(--black); }
  .brand { position: absolute; left: 24px; top: 18px; display: flex; align-items: center; gap: 8px; }
  .brand-square { width: 26px; height: 26px; background: var(--green); }
  .brand-name { font-family: "Open Sans", Arial, sans-serif; font-weight: 700; font-size: 17px; color: var(--white); }
  .ip-note { position: absolute; right: 170px; top: 9px; font-size: 9px; color: #bbbbbb; }
  .ip-note b { color: var(--green); font-weight: 600; }
  .search { position: absolute; right: 22px; top: 6px; display: flex; }
  .search-field { width: 112px; height: 16px; background: var(--white); font-size: 8px; color: #999; padding: 3px 5px; }
  .search-go { width: 28px; height: 16px; background: var(--green); color: var(--white); font-size: 8px; font-weight: 700; text-align: center; line-height: 16px; }
  .main-nav { position: absolute; right: 22px; top: 40px; display: flex; gap: 19px; }
  .main-nav a { color: var(--white); text-decoration: none; font-size: 11px; letter-spacing: .3px; }
  .main-nav a.active { color: var(--green); }

  .hero { position: absolute; top: 66px; left: 0; width: 710px; height: 380px; }
  .hero-photo { position: absolute; inset: 0; background: linear-gradient(100deg, #4d4d4d 0%, #6b6660 40%, #8a7a6a 62%, #5a544e 80%, #3c3a38 100%); }
  .hero-content { position: absolute; left: 47px; top: 62px; }
  .hero-title { font-family: "Roboto Condensed", Arial, sans-serif; font-weight: 700; font-size: 33px; line-height: 36px; color: var(--white); text-transform: uppercase; }
  .hero-sub { margin-top: 12px; font-size: 12px; line-height: 16px; color: var(--white); width: 330px; }
  .code-form { margin-top: 26px; display: flex; gap: 6px; }
  .code-field { width: 180px; height: 24px; background: var(--white); font-size: 9px; color: #777; padding: 6px 8px; }
  .code-button { width: 100px; height: 24px; background: var(--green); color: var(--white); font-size: 10px; font-weight: 700; text-align: center; line-height: 24px; }
  .more-services { position: absolute; right: 26px; top: 254px; font-size: 10px; color: var(--white); }

  .services { position: absolute; top: 344px; left: 20px; width: 670px; height: 214px; background: var(--panel); padding: 26px 28px; display: grid; grid-template-columns: 1fr 1fr; row-gap: 26px; column-gap: 30px; }
  .service { display: flex; gap: 16px; align-items: flex-start; }
  .service-icon { flex: none; width: 62px; height: 62px; border-radius: 50%; background: var(--light); display: flex; align-items: center; justify-content: center; }
  .service-title { font-family: "Roboto Condensed", Arial, sans-serif; font-weight: 700; font-size: 14px; color: var(--green); text-transform: uppercase; margin: 4px 0 4px; }
  .service-text { font-size: 9px; line-height: 12px; color: #b5b5b5; width: 220px; }

  .clients-title { position: absolute; top: 596px; left: 0; width: 710px; text-align: center; font-size: 23px; color: var(--heading); }
  .client { position: absolute; top: 660px; width: 200px; }
  .client-photo { width: 74px; height: 74px; border-radius: 50%; margin-left: 60px; background: radial-gradient(circle at 50% 40%, #e8cdb4 0%, #c9a88c 45%, #dcdcdc 75%); }
  .client-quote { margin-top: 26px; font-size: 9px; line-height: 12px; color: var(--text); }
  .client-name { margin-top: 8px; font-size: 11px; font-weight: 700; color: var(--heading); }
  .client-role { font-size: 9px; color: var(--green); }

  .partners { position: absolute; top: 965px; left: 0; width: 710px; display: flex; justify-content: center; gap: 48px; align-items: center; }
  .partner { background: #c9c9c9; border-radius: 4px; height: 26px; }

  .site-footer { position: absolute; top: 1034px; left: 0; width: 710px; height: 140px; background: var(--footer); color: #aaaaaa; }
  .footer-about { position: absolute; left: 24px; top: 18px; display: flex; gap: 10px; }
  .footer-square { width: 34px; height: 34px; background: var(--green); flex: none; }
  .footer-about p { font-size: 8px; line-height: 11px; width: 110px; color: #cccccc; }
  .copyright { position: absolute; left: 24px; top: 112px; font-size: 8px; color: #cccccc; }
  .footer-heading { font-family: "Roboto Condensed", Arial, sans-serif; font-weight: 700; font-size: 14px; color: var(--white); text-transform: uppercase; }
  .footer-services { position: absolute; left: 250px; top: 14px; }
  .footer-services ul { list-style: none; display: inline-block; vertical-align: top; width: 118px; margin-top: 8px; }
  .footer-services li { font-size: 8px; line-height: 12px; color: #cccccc; }
  .footer-connect { position: absolute; left: 530px; top: 14px; width: 160px; }
  .social { display: flex; gap: 5px; margin-top: 8px; }
  .social span { width: 15px; height: 15px; border-radius: 50%; background: #555555; }
  .newsletter-note { margin-top: 8px; font-size: 7px; line-height: 10px; color: #cccccc; }
  .newsletter { display: flex; margin-top: 8px; }
  .newsletter-field { width: 104px; height: 16px; background: var(--white); font-size: 7px; color: #888; padding: 4px 5px; }
  .newsletter-button { width: 50px; height: 16px; background: var(--green); color: var(--white); font-size: 7px; text-align: center; line-height: 16px; }

  .bottom-nav { position: absolute; top: 1174px; left: 0; width: 710px; height: 26px; text-align: center; font-size: 9px; line-height: 26px; color: #444444; }
</style>
</head>
<body>

<header class="site-header">
  <div class="brand"><span class="brand-square"></span><span class="brand-name">Kelvar Systems</span></div>
  <div class="ip-note">Your IP address is <b>111.222.333.444</b></div>
  <div class="search"><span class="search-field">search...</span><span class="search-go">GO</span></div>
  <nav class="main-nav">
    <a class="active">HOME</a><a>CLIENTS</a><a>SERVICES</a><a>SUPPORT</a><a>TESTIMONIALS</a><a>CONTACT US</a><a>ABOUT US</a>
  </nav>
</header>

<section class="hero">
  <div class="hero-photo" role="img" aria-label="Technician working at a computer in an office"></div>
  <div class="hero-content">
    <h1 class="hero-title">Company with<br>a single objective</h1>
    <p class="hero-sub">To excel in the support and service of all computer and IT needs.</p>
    <div class="code-form"><span class="code-field">Enter your 4-digit code</span><span class="code-button">CONNECT NOW</span></div>
  </div>
  <div class="more-services">+ more services</div>
</section>

<section class="services">
  <div class="service">
    <div class="service-icon"><svg width="30" height="30" viewBox="0 0 30 30" fill="none" stroke="#2a2a2a" stroke-width="3" stroke-linecap="round"><path d="M6 24 L20 10"/><circle cx="22" cy="8" r="4"/><path d="M24 24 L10 10"/><path d="M6 6 L10 10"/></svg></div>
    <div><h3 class="service-title">On-site service</h3><p class="service-text">Our technicians come to your office to fix faults, set up new machines and keep every workstation running smoothly daily.</p></div>
  </div>
  <div class="service">
    <div class="service-icon"><svg width="32" height="30" viewBox="0 0 32 30" fill="none" stroke="#2a2a2a" stroke-width="2.5"><rect x="3" y="4" width="26" height="17" rx="1"/><path d="M12 26 H20 M16 21 V26"/></svg></div>
    <div><h3 class="service-title">Web design</h3><p class="service-text">We plan, design and build clean websites that load fast, work on every screen and are simple to update yourself.</p></div>
  </div>
  <div class="service">
    <div class="service-icon"><svg width="30" height="32" viewBox="0 0 30 32" fill="none" stroke="#2a2a2a" stroke-width="2.5" stroke-linejoin="round"><path d="M15 3 L26 7 V15 C26 22 21 27 15 29 C9 27 4 22 4 15 V7 Z"/><path d="M10 16 L14 20 L21 12"/></svg></div>
    <div><h3 class="service-title">Server &amp; security</h3><p class="service-text">We install servers, firewalls and backups so your data stays protected and your whole network stays online day and night.</p></div>
  </div>
  <div class="service">
    <div class="service-icon"><svg width="32" height="32" viewBox="0 0 32 32" fill="none" stroke="#2a2a2a" stroke-width="3"><circle cx="16" cy="16" r="6"/><path d="M16 3 V8 M16 24 V29 M3 16 H8 M24 16 H29 M7 7 L10.5 10.5 M21.5 21.5 L25 25 M25 7 L21.5 10.5 M10.5 21.5 L7 25"/></svg></div>
    <div><h3 class="service-title">Hardware &amp; software</h3><p class="service-text">We supply and configure desktops, laptops, printers and licensed software, matched to your budget and ready to use on delivery.</p></div>
  </div>
</section>

<h2 class="clients-title">Our Satisfied Clients</h2>

<article class="client" style="left:34px">
  <div class="client-photo" role="img" aria-label="Portrait of Dennis Halloway"></div>
  <p class="client-quote">Their team answered every call within minutes and solved problems we had lived with for years. Our office network has never been this fast, stable and so easy to manage.</p>
  <p class="client-name">Dennis Halloway</p>
  <p class="client-role">Accounting Officer</p>
</article>
<article class="client" style="left:262px">
  <div class="client-photo" role="img" aria-label="Portrait of Richard Jensen"></div>
  <p class="client-quote">Moving our records to a new server felt daunting, but the changeover happened overnight without a single lost file. The staff explained every step in clear, plain and friendly language.</p>
  <p class="client-name">Richard Jensen</p>
  <p class="client-role">Accounting Officer</p>
</article>
<article class="client" style="left:492px">
  <div class="client-photo" role="img" aria-label="Portrait of Clarissa Moreau"></div>
  <p class="client-quote">We rely on them for our pharmacy systems, backups and security updates. Support is quick, honest and fairly priced, and we always know exactly who to call when something breaks.</p>
  <p class="client-name">Clarissa Moreau</p>
  <p class="client-role">President, CEO of Brightwell</p>
</article>

<div class="partners">
  <span class="partner" style="width:48px"></span>
  <span class="partner" style="width:92px"></span>
  <span class="partner" style="width:34px;border-radius:50%;height:34px"></span>
  <span class="partner" style="width:66px"></span>
  <span class="partner" style="width:92px"></span>
</div>

<footer class="site-footer">
  <div class="footer-about">
    <span class="footer-square"></span>
    <p>Kelvar Systems is an Adelaide based company with a single objective - to excel in the support and service of all computer and IT needs.</p>
  </div>
  <p class="copyright">Copyright © 2013 Kelvar Systems Pty Ltd</p>
  <div class="footer-services">
    <h4 class="footer-heading">Services</h4>
    <ul><li>On-site Service</li><li>Remote Desktop Support</li><li>Medical IT Service</li><li>Pharmacy IT Service</li></ul><ul><li>Website Design</li><li>Disaster Recovery</li><li>Hardware/ Software supply</li><li>Consumables</li></ul>
  </div>
  <div class="footer-connect">
    <h4 class="footer-heading">Connect with us</h4>
    <div class="social"><span></span><span></span><span></span><span></span><span></span><span></span></div>
    <p class="newsletter-note">subscribe to our monthly newsletter and get the best deals and discounts</p>
    <div class="newsletter"><span class="newsletter-field">email address</span><span class="newsletter-button">subscribe</span></div>
  </div>
</footer>

<nav class="bottom-nav">Home | Clients | Services | Supports | Testimonials | Contact Us | About us</nav>

</body>
</html>
```